Book Cover Design Project - SIMPLE ART, Pre-Concepted

We already have a full design concept for the cover art. It is however in a low quality word document format. This project is to recreate existing example guideline art in as much vector art possible for great quality print production. Artistic flare is welcome. This will be for a book cover (front/back) and I want the quality to be excellent.

Art to be provided in Adobe Illustrator format. The book will be 6wide x 9high, so the artboard for the cover needs to be set up to 12.5 wide x 9 high with .125" bleeds.

Copy content for the spine: "Beneath a Copper Evening Sky Still" RL Moskowicz.

Here is a link to download the word document "template" and a new photo for the back page. I'm not sure that I like the new photo, it is possible the old one in the word document will work.

www.bluemarlinpressworks.com/uploads/QuillHavenSharedFiles.zip

I've got a fast deadline on this project because the client would like to have manufacturing completed by Christmas...which is why this is only a 2 day project. I appreciate your interest in our project.

Gordon

Try this link...seems I was missing the .zip extension which may have been causing problems.

Requirements
Must have
• Adobe Illustrator Files
CMYK color setup - no color definitions for project
Artboard Size: 12.625 wide x 9.125 high
Art Orientation: Flat image should have the back book page on the left side, front page on the right side, spine copy running down the middle.

```html
<!DOCTYPE html>
<html lang="en">
<head>
<meta charset="utf-8">
<title>Beneath a Copper Evening Sky Still – Book Cover</title>
<link rel="stylesheet" href="https://fonts.googleapis.com/css2?family=Delius&family=PT+Sans:wght@400;700&family=Kaushan+Script&display=swap">
<style>
  :root {
    --blue: #1c74bb;
    --navy: #0d2233;
    --black: #020305;
    --yellow: #ffd41c;
    --gold-dark: #c6942a;
    --gold-light: #fff3c4;
    --teal-glow: #2f5f63;
    --text-light: #e9eef3;
    --line: #6b6f75;
    --white: #ffffff;
  }
  * { margin: 0; padding: 0; box-sizing: border-box; }
  html, body {
    width: 1200px; height: 867px; overflow: hidden; background: var(--white);
  }
  .cover {
    position: relative; width: 1200px; height: 867px; overflow: hidden;
    font-family: "PT Sans", sans-serif;
  }

  /* Back cover */
  .back {
    position: absolute; left: 0; top: 0; width: 577px; height: 867px;
    background: linear-gradient(90deg, var(--blue) 0%, #15507f 45%, var(--navy) 75%, var(--black) 100%);
  }
  .back-title {
    position: absolute; left: 0; top: 48px; width: 577px; text-align: center;
    font-family: "Delius", cursive; font-variant: small-caps; font-weight: 700;
    color: var(--yellow); font-size: 22px; line-height: 25px; letter-spacing: 0.3px;
  }
  .author-photo {
    position: absolute; left: 42px; top: 185px; width: 106px; height: 139px;
    background: linear-gradient(160deg, #9a8f86 0%, #4b4a55 55%, #1f2430 100%);
  }
  .about {
    position: absolute; left: 42px; top: 183px; width: 527px;
    color: var(--text-light); font-size: 10px; line-height: 13.6px;
  }
  .about p { margin-bottom: 13px; }
  .about .lead { margin-left: 116px; }
  .about .label { color: var(--yellow); font-weight: 700; font-size: 11px; }
  .barcode-box {
    position: absolute; left: 309px; top: 721px; width: 189px; height: 104px;
    background: var(--white); border-radius: 12px;
  }

  /* Spine */
  .spine {
    position: absolute; left: 577px; top: 0; width: 49px; height: 867px;
    background: var(--black);
    border-left: 1px solid var(--line); border-right: 1px solid var(--line);
  }
  .spine-text {
    position: absolute; left: 50%; top: 50%;
    transform: translate(-50%, -50%) rotate(90deg);
    white-space: nowrap;
    font-family: "Delius", cursive; font-variant: small-caps; font-weight: 700;
    color: var(--yellow); font-size: 21px;
  }

  /* Front cover */
  .front {
    position: absolute; left: 626px; top: 0; width: 574px; height: 867px;
    background: radial-gradient(ellipse 250px 270px at 280px 357px, var(--teal-glow) 0%, #173033 40%, #070b0c 75%, var(--black) 100%);
  }
  .gold-band {
    position: absolute; left: 0; width: 574px;
    background: linear-gradient(90deg, var(--gold-dark) 0%, var(--gold-light) 50%, var(--gold-dark) 100%);
  }
  .gold-band.top { top: 24px; height: 29px; }
  .gold-band.bottom { top: 783px; height: 52px; }
  .cross { position: absolute; left: 180px; top: 227px; }
  .title-word {
    position: absolute; font-family: "Delius", cursive; font-variant: small-caps;
    font-weight: 700; color: var(--yellow); font-size: 42px; line-height: 1; white-space: nowrap;
  }
  .title-top { left: 0; width: 560px; top: 114px; text-align: center; }
  .title-left { left: 12px; top: 312px; }
  .title-right { right: 16px; top: 312px; }
  .title-bottom { left: 0; width: 560px; top: 608px; text-align: center; }
  .subtitle {
    position: absolute; left: 0; width: 560px; top: 747px; text-align: center;
    font-family: "Kaushan Script", cursive; color: var(--white); font-size: 13px;
  }
</style>
</head>
<body>
<div class="cover">

  <section class="back">
    <h2 class="back-title">"Beneath a Copper Evening Sky Still"<br>RL Moskowicz</h2>
    <div class="author-photo" role="img" aria-label="Portrait photograph of the author"></div>
    <div class="about">
      <p class="lead"><span class="label">About the author:</span> The word of God says that "I know the plans I have for you" (Jeremiah 29:11) and that "before I formed you in the womb I knew you" (Jeremiah 1:5). These verses of scripture depict the life of Raymond L Moskowicz.</p>
      <p class="lead">As a little boy Raymond was always told that he was going to be a preacher. The magnitude of this repeated statement and exactly what it entailed was not taken seriously or truly understood, at that time. It was not Raymond's plan or desire to be a preacher, and he tried to do anything and everything to avoid the talks of him becoming</p>
      <p style="margin-top:-13px">one. Raymond's path of life, although he believed in God, took him down the road that led him away from God. His struggles with life's events and being an introvert kept him emotionally troubled, in a state of depression and wanting to commit suicide. Yet, as the Lord was with Jeremiah, even so was the Lord with Raymond. The Lord was to show Raymond just what it meant to have complete trust in Him and to know that He would always provide a way of an escape. Before Raymond came to the point of carrying out his plans to commit suicide, he prayed a simple prayer that God would give him a new family. At that exact moment Raymond's life began to take a new direction. He began to seek after the Lord; it became his quest to find out what it meant to be a servant of God. Because of his being an introvert, he began to write his emotions on paper in the form of poems. Those poems gave him the strength to come out of depression and began his two year journey to find God.</p>
      <p>Raymond's relationship with Jesus and salvation journey began at the age of nineteen. The poetry writing started as a therapeutic remedy for his troubled past, but developed into the psalms of Raymond because of God's grace and mercy that delivered him from despair and hopelessness.</p>
      <p>God's favor covers Raymond's life and carries him from day to day. It is written that "without me (Christ) ye can do nothing" (John 15:5). This scripture resonates in Raymond's heart. For, he truly believes that God is the author and he is just the vessel used of God. His desire is that each poem will be taken personally and become a tool used by everyone to help them on their Christian journey and to let them know that they are never alone in their experience and quest to be closer to the Lord Jesus Christ.</p>
    </div>
    <div class="barcode-box"></div>
  </section>

  <section class="spine">
    <div class="spine-text">"Beneath a Copper Evening Sky Still" RL Moskowicz</div>
  </section>

  <section class="front">
    <div class="gold-band top"></div>
    <h1 class="title-word title-top">Beneath a</h1>
    <svg class="cross" width="202" height="320" viewBox="0 0 202 320" aria-hidden="true">
      <rect x="66" y="0" width="68" height="320" fill="var(--white)"/>
      <rect x="0" y="72" width="202" height="63" fill="var(--white)"/>
    </svg>
    <span class="title-word title-left">Copper</span>
    <span class="title-word title-right">Evening</span>
    <span class="title-word title-bottom">Sky Still</span>
    <p class="subtitle">A compilation of poems by RL Moskowicz</p>
    <div class="gold-band bottom"></div>
  </section>

</div>
</body>
</html>
```